Corporate Identity Pack - LetterHead, Business Card, Envelope

We are looking for a clean, professional, and visually connected corporate identity set for our company "VELTA HOME" (Cleaning, Gardening, and Pest Control services).

The pack must include:

Business Card (front and back)
Envelope with recipient window on the right side (22x11)
A4 Letterhead

We provide:
Our final logo (PNG)
Three design references (Inspiration1, Inspiration2, Inspiration3) to spark ideas — but you are absolutely free to propose your own creative solutions based on these concepts.

What we want:
A clean, modern, and trustworthy style
A subtle but creative watermark or graphic detail on the letterhead (not too invasive)

The same visual "family feeling" across business card, envelope, and letterhead: designs must be different but clearly connected

Strong readability for all text and contact details

Use our brand colors (Navy Blue, Green, Orange/Red) in a smart, non-overloaded way

No strict limitations: we are open to creative proposals as long as they are coherent, elegant, and suitable for professional use

Technical specifications:
100% full A4 page layout (no accidental borders)

Deliver ready-to-print PDFs and vector files (AI, EPS)

Respect 5 mm safety margins

Standard sizes for A4, business card, envelope C6 with window at the right

Tone:
Modern – Clean – Elegant – Creative – Trustworthy

Target Market(s)

Professional businesses, property managers, condominium administrators, companies, clinics, and offices requiring cleaning, gardening, and pest control services. The design must convey trust, reliability, professionalism, and attention to detail.

Industry/Entity Type

Cleaning Services, Gardening Services, Pest Control Services

Colors
0054AA
0677BA
7BADD7
CADEEF
E8F1F8
59FF00
82FF00
B8FF75
E3FFCB
F4FFEA
EB3D1F
EC4F4E
F09395
F8D3D4
FCEDEE

Requirements
Must have
• Cohesive design across business card, letterhead, and envelope Clean, modern, professional look Use of brand colors: Navy Blue (main), Green, Orange/Red accents Letterhead must include a subtle watermark without interfering with text Envelope must be with a transparent window for recipient address visibility High readability of all text and contact details Proper alignment, no unnecessary margins (full A4 layout)
Nice to have
• Creative but discreet use of the checkmark from the logo as part of the background or watermark Slight variation or accent of color tones while respecting brand identity A clean visual accent that gives a sense of movement or dynamic professionalism (without being distracting) Icons for email, phone, and website on the business card (if stylistically appropriate)
Should not have
• Overuse of colors or rainbow effects Heavy backgrounds or complex textures that interfere with readability Fonts that are too playful, comic-style, or non-professional Overcrowded layouts — the design must feel clean and spacious Watermarks that are too strong or central (they must be subtle and marginal)

```html
<!DOCTYPE html>
<html lang="en">
<head>
<meta charset="utf-8">
<title>VELTA HOME – Business Card</title>
<link rel="stylesheet" href="https://fonts.googleapis.com/css2?family=Raleway:wght@400;700;800&family=Roboto:wght@400&display=swap">
<style>
  :root {
    --stage: #d1d2d4;
    --paper: #ffffff;
    --navy: #27245f;
    --navy-deep: #1d1a52;
    --navy-soft: #5c5894;
    --green: #6cbd45;
    --orange: #f26722;
    --ink: #4f4f55;
    --tint: #ecebf4;
  }
  * { box-sizing: border-box; margin: 0; padding: 0; }
  html, body { width: 1200px; height: 1000px; overflow: hidden; }
  body { background: var(--stage); position: relative; font-family: "Roboto", Arial, sans-serif; }

  .card { position: absolute; left: 281px; width: 637px; height: 364px; }
  .card--front { top: 124px; background: var(--paper); box-shadow: 4px 5px 8px rgba(0,0,0,.18); }
  .card--back { top: 511px; height: 365px; background: var(--navy-deep); box-shadow: 4px 5px 8px rgba(0,0,0,.22); }

  .card__decor { position: absolute; left: 320px; top: 26px; width: 310px; height: 336px; }
  .card__pattern { position: absolute; inset: 0; width: 100%; height: 100%; }

  .brand { position: absolute; left: 56px; top: 53px; z-index: 1; }
  .brand__row { display: flex; align-items: center; gap: 14px; }
  .brand__square { width: 42px; height: 42px; background: var(--navy); }
  .brand__name { font-family: "Raleway", Arial, sans-serif; font-weight: 800; font-size: 33px; color: var(--navy); letter-spacing: .5px; line-height: 1; }
  .brand__services { margin: 4px 0 0 58px; font-family: "Raleway", Arial, sans-serif; font-weight: 700; font-size: 10px; letter-spacing: .4px; color: var(--navy); white-space: nowrap; }

  .person { position: absolute; left: 57px; top: 127px; }
  .person__name { font-family: "Raleway", Arial, sans-serif; font-weight: 400; font-size: 24px; color: var(--navy); letter-spacing: .3px; line-height: 30px; }
  .person__name strong { font-weight: 700; }
  .person__role { margin-top: 0; font-size: 16.5px; line-height: 22px; color: var(--green); }

  .address { position: absolute; left: 57px; top: 193px; font-size: 18px; line-height: 24px; color: var(--ink); }

  .contacts { position: absolute; left: 56px; top: 248px; list-style: none; }
  .contacts li { display: flex; align-items: center; gap: 11px; height: 26.5px; font-size: 18px; color: var(--ink); }
  .contacts svg { width: 21px; height: 21px; flex: none; }
</style>
</head>
<body>

<section class="card card--front">
  <div class="card__decor">
    <svg class="card__pattern" viewBox="0 0 310 336" role="img" aria-label="Faint stepped cluster of brand-symbol watermarks">
      <defs>
        <linearGradient id="decor-fade" x1="1" y1="0" x2="0" y2="1">
          <stop offset="0" stop-color="#ecebf4"/>
          <stop offset=".6" stop-color="#f5f5f9"/>
          <stop offset="1" stop-color="#fbfbfd"/>
        </linearGradient>
      </defs>
      <path d="M192 0H284V336H3V222H107V134H192Z" fill="url(#decor-fade)"/>
    </svg>
  </div>

  <div class="brand">
    <div class="brand__row">
      <div class="brand__square"></div>
      <span class="brand__name">VELTA HOME</span>
    </div>
    <p class="brand__services">CLEANING·GARDENING·PESTCONTROL</p>
  </div>

  <div class="person">
    <h1 class="person__name">DARIO <strong>FENWICK</strong></h1>
    <p class="person__role">Managing Director</p>
  </div>

  <p class="address">218 W Linden Ave Glenmoor,<br>CA 91502</p>

  <ul class="contacts">
    <li>
      <svg viewBox="0 0 21 21" aria-hidden="true"><rect x="1" y="1" width="19" height="19" rx="4" fill="none" stroke="var(--orange)" stroke-width="1.6"/><path d="M6 8c0-1.5 2-2.5 4.5-2.5S15 6.5 15 8l-2 .6-.6-1.2h-3.8L8 8.6zM7.5 10h6l1 5h-8z" fill="var(--orange)"/></svg>
      +39 312 5508214
    </li>
    <li>
      <svg viewBox="0 0 21 21" aria-hidden="true"><rect x="1" y="1" width="19" height="19" rx="4" fill="none" stroke="var(--orange)" stroke-width="1.6"/><rect x="5" y="6.5" width="11" height="8" fill="var(--orange)"/><path d="M5 6.5l5.5 4.5 5.5-4.5" fill="none" stroke="#fff" stroke-width="1.2"/></svg>
      office@velta-home.srl
    </li>
    <li>
      <svg viewBox="0 0 21 21" aria-hidden="true"><rect x="1" y="1" width="19" height="19" rx="4" fill="none" stroke="var(--orange)" stroke-width="1.6"/><circle cx="10.5" cy="10.5" r="5" fill="var(--orange)"/></svg>
      www.velta-home.srl
    </li>
  </ul>
</section>

<section class="card card--back">
  <svg class="card__pattern" viewBox="0 0 637 365" preserveAspectRatio="none" role="img" aria-label="Embossed grid of brand-symbol tiles on navy">
    <defs>
      <linearGradient id="back-fade" x1="0" y1="0" x2="1" y2="0">
        <stop offset="0" stop-color="#5c5894"/>
        <stop offset=".55" stop-color="#3b3775"/>
        <stop offset="1" stop-color="#1d1a52"/>
      </linearGradient>
    </defs>
    <rect width="637" height="365" fill="url(#back-fade)"/>
  </svg>
</section>

</body>
</html>
```